Catalog for our Gold Coins for high value market

We need someone who makes our catalog or book for the gold coins of Switzerland.
Please use the Word Document. The text and the images are below. Feel free to make a nice design. Also make a nice design as a title.
Please use Adobe Indesign or Illustrator to make the content adjustable for us if needed.

You could also add a "star rating" from 1-4 for some of the coins with an image. I will do the rating later. It should be a rating of how precious the coins are without entering a price.
You could also adjust the title design with the coins.

Please make at least the following pages:
Title
Table of content
Title Page for each Ares (Aargau Page 6, Appenzell Page 6, Basel Page 8 and so on)
Pages with the content (Coins including the description)

Target Market(s)

Gold coins collectors. Usually those people are rich men.

Requirements
Must have
• Modern design
Should not have
• Not too many colors used. It should be modern. But have some class.

```html
<!DOCTYPE html>
<html lang="de">
<head>
<meta charset="UTF-8">
<title>Goldmünzen 2023 – Katalog</title>
<link rel="stylesheet" href="https://fonts.googleapis.com/css2?family=DM+Serif+Display&family=Inter:wght@300;400;600&display=swap">
<style>
  :root {
    --gutter: #b3b3b3;
    --paper: #ffffff;
    --slate: #5e6267;
    --gold: #d8c27e;
    --ink: #5a5a5a;
    --wine: #9a1f1c;
    --coin-light: #f6df8a;
    --coin-mid: #e2b94a;
    --coin-dark: #b98a22;
  }
  * { margin: 0; padding: 0; box-sizing: border-box; }
  html, body { width: 911px; height: 1200px; overflow: hidden; background: var(--gutter); }
  .cover {
    width: 911px; height: 1200px;
    display: grid;
    grid-template-columns: 248px 354px 287px;
    grid-template-rows: 302px 281px 273px 311px;
    gap: 11px;
    background: var(--gutter);
  }
  .cell {
    background: var(--paper);
    display: flex; align-items: center; justify-content: center;
  }
  .coin {
    border-radius: 50%;
    background: radial-gradient(circle at 40% 35%, var(--coin-light) 0%, var(--coin-mid) 55%, var(--coin-dark) 100%);
    box-shadow: inset 0 0 0 4px rgba(150,105,20,.35);
  }
  .coin--small { width: 172px; height: 172px; }
  .coin--large { width: 232px; height: 232px; }
  .coin--xl { width: 250px; height: 250px; }
  .coin--wide { width: 252px; height: 252px; }
  .label-cell {
    background: var(--slate);
    position: relative;
    display: block;
  }
  .label-cell__title {
    position: absolute; left: 0; right: 0; top: 105px;
    text-align: center;
    font-family: "DM Serif Display", serif;
    font-size: 36px; color: #fff; letter-spacing: -0.3px;
  }
  .label-cell__mark { position: absolute; left: 112px; top: 174px; }
  .masthead {
    grid-column: 1 / -1;
    background: var(--paper);
    position: relative;
  }
  .masthead__year {
    position: absolute; left: 67px; top: 68px;
    font-family: "Inter", sans-serif; font-weight: 600;
    font-size: 20px; color: var(--ink);
  }
  .masthead__year span { font-size: 15px; margin-right: 4px; position: relative; top: -2px; }
  .masthead__title {
    position: absolute; left: 52px; top: 118px;
    font-family: "DM Serif Display", serif;
    font-size: 84px; line-height: 1; color: var(--gold); letter-spacing: -1px;
  }
  .masthead__subtitle {
    position: absolute; left: 55px; top: 207px;
    font-family: "Inter", sans-serif; font-weight: 400;
    font-size: 21px; color: var(--wine);
  }
</style>
</head>
<body>
  <main class="cover">
    <div class="cell"><div class="coin coin--small" role="img" aria-label="Goldmünze Bern mit gekröntem Wappen"></div></div>
    <div class="cell"><div class="coin coin--large" role="img" aria-label="Goldmünze mit Greif und Umschrift"></div></div>
    <div class="cell label-cell">
      <p class="label-cell__title">Goldmünzen</p>
      <svg class="label-cell__mark" width="60" height="60" viewBox="0 0 60 60" aria-hidden="true">
        <line x1="2" y1="58" x2="58" y2="4" stroke="#b9bcc0" stroke-width="1"/>
        <line x1="8" y1="58" x2="56" y2="12" stroke="#8e9297" stroke-width="1"/>
      </svg>
    </div>

    <div class="cell"><div class="coin coin--small" role="img" aria-label="Goldmünze Kanton Solothurn 1813"></div></div>
    <div class="cell"><div class="coin coin--xl" role="img" aria-label="100 Franken Goldmünze 1925"></div></div>
    <div class="cell"><div class="coin coin--wide" role="img" aria-label="20 Franken Goldmünze 1888 mit Schweizerkreuz"></div></div>

    <div class="cell"><div class="coin coin--small" role="img" aria-label="Goldmünze Kanton Solothurn 1813"></div></div>
    <div class="cell"><div class="coin coin--xl" role="img" aria-label="100 Franken Goldmünze 1925"></div></div>
    <div class="cell"><div class="coin coin--wide" role="img" aria-label="20 Franken Goldmünze 1888 mit Schweizerkreuz"></div></div>

    <header class="masthead">
      <p class="masthead__year"><span>»</span>2023</p>
      <h1 class="masthead__title">Goldmünzen</h1>
      <p class="masthead__subtitle">der Kantone und Eidgenossenschaft</p>
    </header>
  </main>
</body>
</html>
```